Biz Cards to match new logo

I'm looking for a business card layout to go with my new logo. I'd like to have one side in colour (purple, with the logo in white) and the other side to be white with the purple logo and contact info in black font: name, address (2 lines), phone, email, fax, website. The logo includes the company name so it doesn't need to be repeated in the text. The font should be legibile to the semi-blind. (I hate small fonts on business cards).

```html
<!DOCTYPE html>
<html lang="en">
<head>
<meta charset="utf-8">
<title>Vesta Analytics – Business Cards</title>
<link href="https://fonts.googleapis.com/css2?family=Arimo:wght@400;700&display=swap" rel="stylesheet">
<style>
  :root {
    --backdrop: #d1d2d4;
    --brand-purple: #6a4187;
    --card-white: #ffffff;
    --ink: #111111;
    --rule: #c9c9cc;
  }
  * { box-sizing: border-box; margin: 0; padding: 0; }
  html, body {
    width: 1200px;
    height: 1000px;
    overflow: hidden;
    background: var(--backdrop);
    font-family: "Arimo", Arial, sans-serif;
  }
  .canvas { position: relative; width: 1200px; height: 1000px; }

  .card {
    position: absolute;
    width: 554px;
    height: 316px;
  }

  /* Front: purple side */
  .card--front {
    left: 610px;
    top: 36px;
    background: var(--brand-purple);
  }
  .card--front .brand {
    position: absolute;
    left: 0;
    right: 0;
    top: 142px;
    display: flex;
    align-items: center;
    justify-content: center;
    gap: 14px;
    color: var(--card-white);
  }
  .card--front .brand-mark {
    width: 26px; height: 26px;
    background: var(--card-white);
  }
  .card--front .brand-name {
    font-weight: 700;
    font-size: 30px;
    letter-spacing: 4px;
    text-transform: uppercase;
  }

  /* Back: contact side */
  .card--back {
    left: 36px;
    top: 254px;
    background: var(--card-white);
  }
  .card--back .brand {
    position: absolute;
    left: 32px;
    top: 78px;
    display: flex;
    align-items: center;
    gap: 8px;
    color: var(--brand-purple);
  }
  .card--back .brand-mark {
    width: 14px; height: 14px;
    background: var(--brand-purple);
  }
  .card--back .brand-name {
    font-weight: 700;
    font-size: 17px;
    letter-spacing: 2px;
    text-transform: uppercase;
  }

  .contact {
    position: absolute;
    left: 32px;
    top: 164px;
    width: 488px;
    color: var(--ink);
    font-size: 17px;
    line-height: 24px;
  }
  .contact-name {
    font-weight: 700;
    font-size: 20px;
    line-height: 24px;
    padding-bottom: 6px;
    border-bottom: 1px solid var(--rule);
  }
  .contact-block {
    padding: 6px 0 8px;
    border-bottom: 1px solid var(--rule);
  }
  .contact-web { padding-top: 6px; }
  .label { font-weight: 700; }
  .gap { display: inline-block; width: 8px; }
</style>
</head>
<body>
<main class="canvas">

  <section class="card card--front" aria-label="Card front">
    <div class="brand">
      <span class="brand-mark"></span>
      <span class="brand-name">Vesta Analytics</span>
    </div>
  </section>

  <section class="card card--back" aria-label="Card back">
    <div class="brand">
      <span class="brand-mark"></span>
      <span class="brand-name">Vesta Analytics</span>
    </div>

    <div class="contact">
      <p class="contact-name">NAME SURNAME</p>
      <div class="contact-block">
        <p><span class="label">A:</span> Address Line 1, Address Line 2, Address Line 3</p>
        <p><span class="label">P:</span> 123-456-7890<span class="gap"></span> <span class="label">F:</span> 123-456-7890</p>
      </div>
      <p class="contact-web"><span class="label">E:</span> name@domain.com<span class="gap"></span> <span class="label">W:</span> www.domainname.com</p>
    </div>
  </section>

</main>
</body>
</html>
```